Elegant, Playful ReDesign of Paperlark Website in wordpress - Budget has been raised

Project Brief: Paperlark Website Redesign in WordPress

Introduction: Paperlark, a cutting-edge document creation solution, aims to revolutionize the tedious process of crafting contracts, offers, forms, and other documents. By saving customers valuable time, streamlining workflows, and minimizing human error, Paperlark has become an essential tool. As a technology company with a diverse clientele, we're set to boost our online presence through a refreshed WordPress website. Beyond a modernized website, we aspire to establish a stronger brand identity, incorporating graphic elements seamlessly into our online presence.

Current Status: Currently hosted on WordPress, Paperlark's existing website serves its purpose but is ready for a visual transformation. Our goal is to maintain a modern and attractive appearance while upholding our commitment to simplicity and efficiency. Notably, the website is currently only in Danish. The redesigned structure should include a language switch function to cater to future international customers.

Objectives:
• Modern Aesthetic: Redesign the website with a fresh and modern vibe, reflecting innovation in the document creation sphere.
• User-Friendly: Prioritize an intuitive design for seamless navigation, ensuring visitors easily understand our offerings and benefits.
• Informative Content: Strike a balance between attractiveness and informativeness, clearly communicating Paperlark's value proposition and simplifying business processes.
• Graphic Elements: Integrate visually appealing graphics that enhance the site's aesthetics and contribute to our overall visual identity. These elements should be versatile for future use in social media, advertisements, and other branding materials.
• Brand Recognition: Maintain our current logo and color scheme while exploring creative ways to establish a distinctive brand identity. The website should be a cornerstone for a cohesive branding strategy.
• Media Integration: Include images or videos on the website to enhance engagement. Find suitable, free-to-use visuals.
• Responsiveness: Ensure the design is responsive and works seamlessly on all devices.
• Demo Booking Form: Improve the design of the form to book a demo.
• Multilingual Support: Enable language transformation; the website is currently in Danish but should cater to other countries.

Guidelines:
• Typography: Up to the designer's discretion.
• Images/Videos: Must be free to use without additional charges.
• WordPress Theme: Use any WordPress theme below $100.
• Logo Redesign: Not needed; stick to the referenced color palette, as our new logo uses these colors.
• Color Palette: Stick to the existing company colors for consistency:
RGB
• #000b3c
• #004c6c
• #319ac3
• Greytones and white are also allowed
• Creativity Encouraged: Embrace creativity within the color palette for the layout, visuals, and overall user experience.

Conclusion: The Paperlark website redesign marks an exciting opportunity to enhance our online presence. Our goal is to achieve a balance between a modern, attractive design and a clear, informative representation of our innovative solutions. We envision the revamped website as the foundation for a compelling online brand presence, with versatile graphic elements resonating across various digital platforms.

Sections that the website must include: Space for customer logos, space for testimonials, Space and redesign for display of price structure and price comparison, sections for company details and other information.

Design should also include a redesign of the customer cases section.
Generally there should just be a redesign of all things that are on the website.

Link to current website: https://paperlark-example.com/

+50 employees.

Document automation

Coded - Design and coding required

5+ page

0054AA
0677BA
7BADD7
CADEEF
E8F1F8

• The new webpage must have the same pages as the current one. Frontpage, Book demo, About us, Case stories and Pricing

```html
<!DOCTYPE html>
<html lang="en">
<head>
<meta charset="utf-8">
<title>Paperlark – Creating signable documents</title>
<link href="https://fonts.googleapis.com/css2?family=Poppins:ital,wght@0,300;0,400;0,500;0,600;1,400&display=swap" rel="stylesheet">
<style>
:root{
  --navy:#000b3c;
  --teal:#0f5f80;
  --teal-deep:#0c4a6b;
  --blue:#1496cf;
  --blue-bright:#1a9ad3;
  --ink:#1c2233;
  --text:#4a4f5a;
  --grey-bg:#f4f4f4;
  --white:#ffffff;
  --star:#f5b417;
}
*{margin:0;padding:0;box-sizing:border-box}
html,body{width:1200px;height:4515px;overflow:hidden}
body{font-family:'Poppins',sans-serif;color:var(--text);background:var(--white);position:relative}
.abs{position:absolute}
a{color:inherit;text-decoration:none}

/* header */
.site-header{position:absolute;left:0;top:0;width:1200px;height:126px;background:var(--white)}
.brand{position:absolute;left:88px;top:36px;display:flex;align-items:center;gap:14px}
.brand-square{width:52px;height:52px;background:var(--blue)}
.brand-name{font-size:32px;font-weight:600;color:var(--teal-deep);letter-spacing:.5px}
.main-nav{position:absolute;left:415px;top:52px;display:flex;gap:21px;font-size:15px;color:#333}
.btn-book{position:absolute;left:974px;top:44px;width:140px;height:39px;border-radius:20px;background:var(--blue);color:#fff;font-size:14px;display:flex;align-items:center;justify-content:center}

/* hero */
.hero-photo{position:absolute;left:0;top:126px;width:1200px;height:606px;background:linear-gradient(110deg,#3d3b3a 0%,#8a8783 18%,#e8e6e2 40%,#f4f3f0 70%,#cfcbc6 100%)}
.hero-panel{position:absolute;left:470px;top:361px;width:730px;height:371px;background:var(--teal);border-radius:140px 0 0 140px}
.hero-title{position:absolute;left:550px;top:422px;font-size:38px;line-height:45px;font-weight:400;color:#fff;letter-spacing:.5px}
.hero-text{position:absolute;left:550px;top:530px;width:560px;font-size:15.5px;line-height:22px;color:#e6f1f6}
.btn-outline{position:absolute;left:550px;top:621px;width:140px;height:40px;border:1.5px solid #fff;border-radius:20px;color:#fff;font-size:15px;display:flex;align-items:center;justify-content:center}

/* section titles */
.section-title{position:absolute;display:flex;align-items:center;gap:16px}
.title-mark{width:64px;height:64px;background:var(--blue)}
.title-main{font-size:41px;line-height:44px;font-weight:500;color:var(--ink)}
.title-main span{color:var(--blue)}
.title-sub{font-size:17px;color:#333;letter-spacing:.5px}

/* about */
.about-photo-a{position:absolute;left:84px;top:925px;width:353px;height:350px;border-radius:80px 0 0 80px;background:linear-gradient(135deg,#e9e7e4,#b8b2ab 55%,#6d635a)}
.about-photo-b{position:absolute;left:285px;top:1120px;width:228px;height:255px;border-radius:70px 0 0 0;background:linear-gradient(160deg,#5a3a26,#2d1a10 60%,#8a6a4a)}
.about-heading{position:absolute;left:564px;top:922px;font-size:24px;font-weight:400;color:var(--teal);letter-spacing:.3px}
.about-body{position:absolute;left:565px;top:978px;width:550px;font-size:15px;line-height:22.5px;color:var(--text)}
.about-body p{margin-bottom:22px}
.btn-solid{position:absolute;height:38px;background:var(--blue);color:#fff;font-size:14px;display:flex;align-items:center;justify-content:center}

/* services */
.band-grey{position:absolute;left:0;width:1200px;background:var(--grey-bg)}
.card{position:absolute;top:1661px;width:330px;height:480px;background:#fff;border-radius:0 0 40px 0}
.card-img{position:absolute;left:10px;top:12px;width:310px;height:205px}
.card h3{position:absolute;left:0;top:252px;width:100%;text-align:center;font-size:19.5px;font-weight:400;color:var(--teal)}
.card p{position:absolute;left:30px;top:289px;width:270px;text-align:center;font-size:15px;line-height:24px}
.card .btn-solid{left:88px;top:397px;width:154px}

/* steps */
.step-circle{position:absolute;width:98px;height:98px;border-radius:50%;background:var(--blue);color:#fff;font-family:Georgia,serif;font-size:46px;display:flex;align-items:center;justify-content:center}
.step-title{position:absolute;width:330px;text-align:center;font-size:19.5px;color:var(--teal)}
.step-text{position:absolute;width:270px;text-align:center;font-size:15px;line-height:26px}

/* video */
.video{position:absolute;left:98px;top:2873px;width:1020px;height:508px;background:linear-gradient(180deg,#b98b57,#c69a66 45%,#8c7060 75%,#514a46)}

/* testimonials */
.avatar{position:absolute;border-radius:50%}
.nav-arrow{position:absolute;width:42px;height:42px;border-radius:50%;background:var(--blue)}
.client-name{position:absolute;left:0;top:3763px;width:1200px;text-align:center;font-size:21px;color:var(--ink)}
.client-role{position:absolute;left:0;top:3792px;width:1200px;text-align:center;font-size:17px;font-style:italic;color:var(--teal)}
.quote{position:absolute;left:235px;top:3866px;width:740px;text-align:center;font-size:15px;line-height:22.5px}

/* footer */
.site-footer{position:absolute;left:0;top:4007px;width:1200px;height:394px;background:var(--blue-bright);color:#fff}
.foot-head{position:absolute;top:93px;font-size:20px;font-weight:400}
.foot-head b{font-weight:600}
.foot-rule{position:absolute;top:130px;width:40px;height:2px;background:#fff}
.foot-links{position:absolute;top:170px;list-style:none;font-size:15px}
.foot-links li{height:31px;display:flex;align-items:center;gap:12px}
.contact-row{position:absolute;left:767px;display:flex;align-items:center;gap:20px;font-size:14.5px;line-height:18px}
.contact-icon{width:34px;height:34px;border:1.5px solid #fff;border-radius:4px;display:flex;align-items:center;justify-content:center}
.bottom-bar{position:absolute;left:0;top:4401px;width:1200px;height:114px;background:var(--teal-deep);color:#fff}
.social{position:absolute;top:32px;width:42px;height:42px;border:2px solid #fff;border-radius:50%}
.copyright{position:absolute;right:86px;top:44px;font-size:15px}
</style>
</head>
<body>

<header class="site-header">
  <a class="brand" href="https://paperlark-example.com/"><span class="brand-square"></span><span class="brand-name">Paperlark</span></a>
  <nav class="main-nav">
    <a>FRONT PAGE</a><a>KUNDECASES</a><a>VIDEO</a><a>LIVE DEMO</a><a>PRICES</a><a>ABOUT US</a>
  </nav>
  <a class="btn-book">BOOK DEMO</a>
</header>

<section>
  <div class="hero-photo" role="img" aria-label="Photo of a contract being handed across a desk"></div>
  <div class="hero-panel"></div>
  <h1 class="hero-title">CREATE FLAWLESS CONTRACTS<br>AND QUOTES QUICKLY</h1>
  <p class="hero-text">Lorem ipsum dolor sit amet, consectetur adipiscing elit, sed do eiusmod tempor incididunt ut labore et dolore magna aliqua. Quis ipsum suspendisse ultrices gravida.</p>
  <a class="btn-outline">Book demo</a>
</section>

<section>
  <div class="section-title" style="left:410px;top:800px">
    <span class="title-mark"></span>
    <div><div class="title-main">ABOUT <span>US</span></div><div class="title-sub">WHO WE ARE</div></div>
  </div>
  <div class="about-photo-a" role="img" aria-label="Photo of a businesswoman at work"></div>
  <div class="about-photo-b" role="img" aria-label="Photo of a desk lamp above stacks of documents"></div>
  <h2 class="about-heading">EXPERTIZE TO CREATE LEGAL DOCUMENTS</h2>
  <div class="about-body">
    <p>Paperlark started with a desire to make it easy and inexpensive to create legal documents. Prices were difficult to compare and the existing templates were difficult to fill out.</p>
    <p>Together with a partner, Mikkel developed an intelligent document solution to bridge the gap between the lawyer and the should be able to create, and it quickly became popular.</p>
    <p>We have continuously experienced demand for automation of offers and client contracts, while we have been focused on the legal industry. Therefore, we have now launched a SaaS solution in Paperlark's own brand, where all types of offers and customer contracts can be created quickly and error-free.</p>
  </div>
  <a class="btn-solid" style="left:564px;top:1303px;width:155px">READ MORE</a>
</section>

<section>
  <div class="band-grey" style="top:1458px;height:746px"></div>
  <div class="section-title" style="left:255px;top:1536px">
    <span class="title-mark"></span>
    <div><div class="title-main">INTEGRATION TIL CRM <span>TIL CRM</span></div><div class="title-sub">WHAT WE DO</div></div>
  </div>
  <article class="card" style="left:93px">
    <div class="card-img" role="img" aria-label="Photo of a handshake over a desk" style="background:linear-gradient(160deg,#6b5a48,#b9ab98 60%,#e8e3da)"></div>
    <h3>DIGITAL SIGNATURE</h3>
    <p>Send your offers for digital signature with data directly from your quickly and easily.</p>
    <a class="btn-solid">READ MORE</a>
  </article>
  <article class="card" style="left:435px">
    <div class="card-img" role="img" aria-label="Photo of a document being passed between hands" style="background:linear-gradient(160deg,#b7b7b5,#e3d2b8 55%,#9a8e84)"></div>
    <h3>AUTOMATED OFFERS</h3>
    <p>Tailor your offers down to the smallest detail and get sections all relevant sections and calculate your prices automatically .</p>
    <a class="btn-solid">READ MORE</a>
  </article>
  <article class="card" style="left:778px">
    <div class="card-img" role="img" aria-label="Photo of a businessman working at a laptop" style="background:linear-gradient(160deg,#d7dadc,#9ea3a8 50%,#eef0f1)"></div>
    <h3>LEADS FRA DIT WEBSITE</h3>
    <p>Manage your leads and customer queries with intelligent forms right on your own website.</p>
    <a class="btn-solid">READ MORE</a>
  </article>
</section>

<section>
  <div class="section-title" style="left:228px;top:2261px">
    <span class="title-mark"></span>
    <div><div class="title-main">INTELLIGENT <span>DOKUMENTLØSNING</span></div><div class="title-sub">WHAT WE DO</div></div>
  </div>
  <div class="step-circle" style="left:191px;top:2393px">1</div>
  <div class="step-circle" style="left:557px;top:2393px">2</div>
  <div class="step-circle" style="left:927px;top:2393px">3</div>
  <svg class="abs" style="left:330px;top:2405px" width="140" height="50" viewBox="0 0 140 50" fill="none" stroke="#1496cf" stroke-width="3" stroke-linecap="round">
    <path d="M5 25 Q60 -5 128 35" stroke-dasharray="1 7"/><path d="M120 30 L130 36 L125 24"/>
  </svg>
  <svg class="abs" style="left:735px;top:2435px" width="140" height="50" viewBox="0 0 140 50" fill="none" stroke="#1496cf" stroke-width="3" stroke-linecap="round">
    <path d="M5 20 Q60 50 125 16" stroke-dasharray="1 7"/><path d="M115 14 L127 14 L122 26"/>
  </svg>
  <div class="step-title" style="left:75px;top:2512px">SELECT DOCUMENT</div>
  <div class="step-title" style="left:441px;top:2512px">UDFYLD GUIDED FLOW</div>
  <div class="step-title" style="left:811px;top:2512px">SIGN DIGITALLY</div>
  <p class="step-text" style="left:105px;top:2550px">Let us evaluate your case to determine your legal options will work directly with you.</p>
  <p class="step-text" style="left:471px;top:2550px">Let us evaluate your case to determine your legal options will work directly with you.</p>
  <p class="step-text" style="left:841px;top:2550px">Let us evaluate your case to determine your legal options will work directly with you.</p>
</section>

<section>
  <div class="band-grey" style="top:2724px;height:731px"></div>
  <div class="section-title" style="left:385px;top:2766px">
    <span class="title-mark"></span>
    <div><div class="title-main">START LIVE <span>DEMO</span></div><div class="title-sub">PLAY VIDEOS</div></div>
  </div>
  <div class="video" role="img" aria-label="Video still of a presenter standing by a corkboard with colleagues at a table"></div>
  <svg class="abs" style="left:572px;top:3092px" width="72" height="72" viewBox="0 0 72 72">
    <circle cx="36" cy="36" r="34" fill="#fff"/><path d="M29 22 L52 36 L29 50 Z" fill="#1496cf"/>
  </svg>
</section>

<section>
  <div class="section-title" style="left:315px;top:3505px">
    <span class="title-mark"></span>
    <div><div class="title-main">WHAT OUR <span>CLIENT SAYS</span></div><div class="title-sub">CLIENTS TESTIMONIALS</div></div>
  </div>
  <div class="avatar" role="img" aria-label="Client portrait" style="left:281px;top:3646px;width:66px;height:66px;background:#8a8a8a"></div>
  <div class="avatar" role="img" aria-label="Client portrait" style="left:400px;top:3637px;width:84px;height:84px;background:#d6a77a"></div>
  <div class="avatar" role="img" aria-label="Client portrait" style="left:550px;top:3625px;width:108px;height:108px;background:#4d4a47"></div>
  <div class="avatar" role="img" aria-label="Client portrait" style="left:725px;top:3637px;width:84px;height:84px;background:#6c5a4c"></div>
  <div class="avatar" role="img" aria-label="Client portrait" style="left:862px;top:3646px;width:66px;height:66px;background:#c9c2bd"></div>
  <svg class="nav-arrow" style="left:135px;top:3777px" viewBox="0 0 42 42"><path d="M24 14 L17 21 L24 28" fill="none" stroke="#fff" stroke-width="3"/></svg>
  <svg class="nav-arrow" style="left:1034px;top:3777px" viewBox="0 0 42 42"><path d="M18 14 L25 21 L18 28" fill="none" stroke="#fff" stroke-width="3"/></svg>
  <div class="client-name">Jonas</div>
  <div class="client-role">Assit Manager</div>
  <svg class="abs" style="left:540px;top:3828px" width="125" height="26" viewBox="0 0 125 26" fill="#f5b417">
    <g id="star"><path d="M12 1 L15 9 L23.5 9.5 L17 15 L19 23.5 L12 19 L5 23.5 L7 15 L0.5 9.5 L9 9 Z"/></g>
    <use href="#star" x="25"/><use href="#star" x="50"/><use href="#star" x="75"/><use href="#star" x="100"/>
  </svg>
  <p class="quote">Lorem ipsum dolor sit amet, consectetur adipiscing elit, sed do eiusmod tempor incididunt ut labore et dolore magna aliqua. Quis ipsum suspendisse ultrices gravida. Risus commodo viverra maecenas accumsan lacus vel facilisis.</p>
</section>

<footer class="site-footer">
  <div class="foot-head" style="left:217px"><b>Quick</b> Links</div>
  <div class="foot-rule" style="left:217px"></div>
  <ul class="foot-links" style="left:220px">
    <li>›&nbsp;Home</li><li>›&nbsp;About Us</li><li>›&nbsp;Live Demo</li><li>›&nbsp;Prices</li><li>›&nbsp;Testimonials</li>
  </ul>
  <div class="foot-head" style="left:499px"><b>Customer</b> Services</div>
  <div class="foot-rule" style="left:499px"></div>
  <ul class="foot-links" style="left:502px">
    <li>›&nbsp;Contact us</li><li>›&nbsp;Site Map</li><li>›&nbsp;Terms and Use</li><li>›&nbsp;My Account</li>
  </ul>
  <div class="foot-head" style="left:767px"><b>Our</b> Newsletter</div>
  <div class="foot-rule" style="left:767px"></div>
  <div class="contact-row" style="top:177px">
    <span class="contact-icon"><svg width="16" height="16" viewBox="0 0 16 16"><path d="M3 1 L6 1 L7 5 L5 6 Q6.5 9.5 10 11 L11 9 L15 10 L15 13 Q8 15 3 9 Q0.5 5 3 1Z" fill="none" stroke="#fff" stroke-width="1.3"/></svg></span>
    <span>CALL US<br>+45 31 07 55 19</span>
  </div>
  <div class="contact-row" style="top:233px">
    <span class="contact-icon"><svg width="16" height="12" viewBox="0 0 16 12"><rect x="1" y="1" width="14" height="10" fill="none" stroke="#fff" stroke-width="1.3"/><path d="M1 1 L8 7 L15 1" fill="none" stroke="#fff" stroke-width="1.3"/></svg></span>
    <span>EMAIL US<br>contact@paperlark-example.com</span>
  </div>
  <div class="contact-row" style="top:291px">
    <span class="contact-icon"><svg width="14" height="18" viewBox="0 0 14 18"><path d="M7 17 Q1 10 1 7 A6 6 0 0 1 13 7 Q13 10 7 17Z" fill="none" stroke="#fff" stroke-width="1.3"/><circle cx="7" cy="7" r="2" fill="#fff"/></svg></span>
    <span>Lindeparken 14, DK-4180<br>Norrebyg</span>
  </div>
</footer>

<div class="bottom-bar">
  <a class="social" style="left:93px" aria-label="Video channel"></a>
  <a class="social" style="left:144px" aria-label="Social profile"></a>
  <a class="social" style="left:196px" aria-label="Social feed"></a>
  <a class="social" style="left:249px" aria-label="Photo profile"></a>
  <div class="copyright">All Rights Reserved @ Copyrights 2023</div>
</div>

</body>
</html>
```